wordpress website Carla Wendt, Author, Speaker and Coach

Need a wordpress blogging website for author/speaker/coach.
I have paid for hosting on siteburrow.
I am currently writing a book - Ladder to Campus - Steps and strategies to prepare you to thrive in college and beyond. Eventually, I will have an Academic/Life Coaching program targeting high school and college students. This website's purpose is to build my email list. I can offer the following reports as incentive for email sign-up:
1. Six Habits That Get Your Teen Through University on Schedule
2. Clever Routes to Fund a Degree
3. QRT/BVT vocabulary word of the day

facebook page: https://www.facebook.com/Carla-Wendt-AcademicLife-Coach-918273645019283/

I would like to have these pages:

1. Home or About page

High school is becoming more and more stressful for students. Not only are they taking more AP classes than ever before, and often spending $1,000’s on QRT/BVT prep programs, most are NOT prepared for success in college. Only 19% of students are graduating from college within 4 years and only 56% are graduating within 6 years. With the cost of higher education skyrocketing, each extra year of school can costs families $40,000 - $60,000 when you factor in living expenses. Then, when students do graduate, they are often underemployed.

Carla's approach is whole person oriented. Her programs help students learn life skills in addition to the study, time management skills, etc. offered by most academic coaching programs. Our program addresses all of the major causes of failure to graduate within 4 years, and is based on sound educational research. Carla's program initially provides the daily interaction needed to successfully change behaviors and seat new success habits, unlike many programs in which students interact with coaches only once a week.
Bio
Carla Wendt is a certified teacher and holds advanced certification in academic coaching and tutoring. She also is a certified trainer in the Morris Pelley Growth Method. She has three successful adult children, and helped them overcome learning differences and thrive.

2. Blog

3. Contact - Include form (I split time between USA and Saudi Arabia, so I will call or email people back, but don't want to leave a phone number)
info@carlawendt.example

4. Store – 1 book for now
Ladder to Campus
Steps and strategies to prepare you to thrive in college and beyond
Available 12/01/2017
I could make a preview chapter available for download

5. Speaking
Carla Wendt is available for keynote addresses and half-day, full day or multi-day workshops. I will develop details later

6.Coaching programs
I will develop details later

Target Market(s)

high school students who are college bound and their parents

Number of Pages Required

5+ page

Font styles to use
Sans Serif

Colors

Designer to choose colors to be used in the design.

Requirements
Nice to have
• integration with post finch for contact management

```html
<!DOCTYPE html>
<html lang="en">
<head>
<meta charset="utf-8">
<title>Carla Wendt – Author, Speaker and Coach</title>
<link href="https://fonts.googleapis.com/css2?family=Lato:ital,wght@0,400;0,700;0,900;1,400;1,700;1,900&family=Open+Sans:wght@400;600;700&display=swap" rel="stylesheet">
<style>
:root{
  --green:#8cc63f;
  --green-dark:#0f7b3f;
  --purple:#8f8fcb;
  --ink:#222;
  --text:#555;
  --light:#f3f3f3;
  --footer:#2a2a2a;
  --footer-bar:#1c1c1c;
  --white:#fff;
}
*{margin:0;padding:0;box-sizing:border-box}
html,body{width:1200px;height:3719px;overflow:hidden;background:var(--white)}
body{font-family:"Lato",sans-serif;color:var(--text);font-size:14px;position:relative}
.section{position:absolute;left:0;width:1200px}
.btn{display:inline-block;font-family:"Lato",sans-serif;font-weight:700;font-size:13px;color:var(--white);text-transform:uppercase;padding:0 26px;height:40px;line-height:40px;border-radius:2px}
.btn-green{background:var(--green)}
.btn-purple{background:var(--purple)}
.btn-outline{border:1px solid rgba(255,255,255,.85)}
.ph{position:absolute}

/* header */
.site-header{top:0;height:70px;background:var(--white);border-bottom:1px solid #e6e6e6}
.brand{position:absolute;left:161px;top:16px;display:flex;align-items:center;gap:10px;font-family:"Lato",sans-serif;font-weight:700;font-size:27px;color:var(--ink)}
.brand-dot{width:30px;height:30px;border-radius:50%;background:var(--green)}
.main-nav{position:absolute;right:160px;top:18px;display:flex;align-items:center;gap:0}
.main-nav a{font-size:13px;color:#444;padding:0 10px;line-height:34px}
.nav-home{width:34px;height:34px;background:var(--green);display:flex;align-items:center;justify-content:center;margin-right:8px}
.nav-search{width:34px;height:34px;border:1px solid #ddd;display:flex;align-items:center;justify-content:center;margin-left:8px}

/* hero */
.hero{top:70px;height:475px}
.hero-bg{left:0;top:0;width:1200px;height:475px;background:linear-gradient(100deg,#3a2a1e 0%,#6e5138 35%,#8a7058 55%,#4d3a2a 80%,#2e2218 100%)}
.hero-copy{position:absolute;left:161px;top:155px;color:var(--white)}
.hero-title{font-family:"Open Sans",sans-serif;font-weight:700;font-size:31px;letter-spacing:.5px}
.hero-sub{font-weight:700;font-size:19px;line-height:28px;margin-top:10px}
.hero-actions{margin-top:28px;display:flex;gap:14px}
.hero-book{left:744px;top:10px;width:297px;height:455px;background:linear-gradient(160deg,#5a5a5a 0%,#3d3d3d 55%,#6c3fa0 75%,#e0c42a 100%);box-shadow:-10px 10px 20px rgba(0,0,0,.35)}
.hero-book span{position:absolute;right:22px;bottom:30px;color:var(--white);font-weight:700;font-size:17px}
.arrow{position:absolute;top:205px}

/* welcome */
.welcome{top:545px;height:405px;background:var(--white)}
.welcome-media{left:161px;top:70px;width:414px;height:258px;background:linear-gradient(135deg,#2b2b2b,#6b5f58 60%,#1d1d1d)}
.welcome-text{position:absolute;left:610px;top:72px;width:430px}
.welcome-text h2{font-family:"Open Sans",sans-serif;font-weight:400;font-size:28px;color:var(--ink);letter-spacing:.5px}
.welcome-text h2 b{font-weight:700}
.welcome-text p{font-size:12.5px;line-height:21px;margin-top:14px;color:#555}
.welcome-text .btn{margin-top:22px;height:28px;line-height:28px;font-size:11px;padding:0 24px}

/* learning band */
.learning{top:950px;height:307px;background:var(--green)}
.learning-photo{left:136px;top:-38px;width:335px;height:325px;background:linear-gradient(180deg,#c7a88c,#4d6fa0 55%,#2d2d4d);border-radius:40% 40% 6px 6px}
.learning-copy{position:absolute;left:486px;top:65px;color:var(--white);width:560px}
.learning-copy h2{font-style:italic;font-weight:900;font-size:27px;letter-spacing:.5px}
.learning-copy p{font-style:italic;font-size:12.5px;line-height:20px;margin-top:14px}
.learning-actions{display:flex;gap:18px;margin-top:28px}
.learning-actions .btn{height:38px;line-height:38px;font-size:12px}

/* programs */
.programs{top:1257px;height:441px;background:var(--light)}
.section-title{font-family:"Open Sans",sans-serif;font-weight:600;font-size:28px;color:var(--ink);text-align:center}
.programs .section-title{margin-top:68px}
.section-lead{text-align:center;font-size:12px;margin-top:8px;color:#555}
.program-card{position:absolute;top:151px;width:422px;height:223px;color:var(--white);text-align:center;box-shadow:0 3px 10px rgba(0,0,0,.12)}
.program-card.coaching{left:161px;background:var(--green-dark)}
.program-card.speaking{left:615px;background:var(--green)}
.program-card svg{margin-top:26px}
.program-card h3{font-family:"Open Sans",sans-serif;font-weight:600;font-size:22px;letter-spacing:1px;margin-top:12px}
.program-card p{font-size:12px;line-height:17px;width:340px;margin:8px auto 0}
.card-btn{display:inline-block;margin-top:12px;background:var(--white);color:var(--green-dark);font-size:12px;padding:0 16px;height:28px;line-height:28px;border-radius:2px}
.speaking .card-btn{color:var(--green)}

/* shop */
.shop{top:1698px;height:501px}
.shop-panel{position:absolute;left:0;top:0;width:600px;height:501px;background:var(--purple)}
.shop-copy{position:absolute;left:161px;top:160px;color:var(--white)}
.shop-copy h2{font-family:"Open Sans",sans-serif;font-weight:600;font-size:26px}
.shop-copy p{font-size:12.5px;line-height:19px;margin-top:14px}
.shop-actions{display:flex;gap:14px;margin-top:18px}
.shop-actions .btn{height:34px;line-height:34px;font-size:12px;padding:0 20px}
.shop-tile{position:absolute;width:300px;height:250px}
.shop-tile .label{position:absolute;left:35px;bottom:8px;width:230px;height:26px;line-height:26px;background:rgba(30,30,30,.78);color:var(--white);font-size:11px;text-align:center}

/* blog */
.blog{top:2199px;height:478px;background:var(--white)}
.blog .section-title{margin-top:28px;font-weight:700;font-size:26px}
.blog-main{position:absolute;left:161px;top:124px;width:501px;height:267px;background:var(--white);box-shadow:0 2px 10px rgba(0,0,0,.12)}
.blog-main .copy{position:absolute;left:25px;top:24px;width:260px}
.blog-main h3{font-family:"Open Sans",sans-serif;font-weight:600;font-size:16px;line-height:22px;color:var(--ink)}
.posted{font-size:10.5px;margin-top:8px;color:#333}
.posted b{font-weight:700}
.blog-main p{font-size:11px;line-height:18px;color:#888;margin-top:14px}
.read-more{font-size:11px;color:#333;margin-top:6px;display:block}
.blog-main .thumb{left:301px;top:0;width:200px;height:267px;background:linear-gradient(160deg,#7a6a58,#c8b59c 50%,#4b3e34)}
.date-tag{position:absolute;left:0;top:0;width:75px;height:58px;background:var(--purple);color:var(--white);font-size:12px;text-align:center;padding-top:8px;line-height:18px}
.blog-side{position:absolute;left:731px;width:298px;height:124px;background:var(--white);box-shadow:0 2px 10px rgba(0,0,0,.12)}
.blog-side .thumb{left:0;top:0;width:130px;height:124px;background:linear-gradient(150deg,#8a5e86,#d9a35d 55%,#4a3a2f)}
.blog-side .date-tag{width:62px;height:48px;font-size:10px;line-height:15px;padding-top:6px}
.blog-side .copy{position:absolute;left:143px;top:14px;width:145px}
.blog-side h4{font-family:"Open Sans",sans-serif;font-weight:600;font-size:12px;line-height:16px;color:var(--ink)}
.blog-side p{font-size:10px;line-height:15px;color:#888;margin-top:6px}
.blog-side .read-more{font-size:10px;margin-top:4px}

/* newsletter */
.newsletter{top:2677px;height:285px;background:var(--green-dark);text-align:center;color:var(--white)}
.newsletter h2{font-family:"Open Sans",sans-serif;font-weight:400;font-size:26px;margin-top:64px}
.newsletter p{font-style:italic;font-size:12px;margin-top:12px}
.subscribe-form{display:flex;justify-content:center;gap:15px;margin-top:18px}
.subscribe-input{width:397px;height:42px;background:var(--white);color:#777;font-size:12px;text-align:left;padding-left:10px;line-height:42px}
.subscribe-btn{width:193px;height:42px;line-height:42px;background:var(--green);font-size:12px;font-weight:700;text-transform:uppercase}

/* testimonials */
.students{top:2962px;height:459px;background:var(--white)}
.students h2{position:absolute;left:161px;top:70px;font-family:"Open Sans",sans-serif;font-weight:700;font-size:26px;color:var(--ink);letter-spacing:.5px}
.students .quote{position:absolute;left:161px;top:163px;width:470px;font-size:11.5px;line-height:19px;color:#444}
.students .name{position:absolute;left:161px;top:322px;font-weight:700;font-size:16px;color:var(--green-dark)}
.students .role{position:absolute;left:161px;top:345px;font-size:11px;color:#666}
.dots{position:absolute;left:161px;top:366px;display:flex;gap:6px}
.dots i{display:block;width:22px;height:4px;background:var(--green)}
.dots i:first-child{background:var(--green-dark)}
.students-photo{left:640px;top:20px;width:540px;height:420px;background:radial-gradient(ellipse at 50% 55%,#e6a15a 0%,#c4834c 35%,#f3f3f3 72%)}

/* footer */
.site-footer{top:3421px;height:253px;background:var(--footer);color:#cfcfcf}
.footer-col{position:absolute;top:50px}
.footer-col h4{font-family:"Open Sans",sans-serif;font-weight:400;font-size:15px;color:var(--white)}
.footer-col .rule{width:235px;height:1px;background:#555;margin:10px 0 12px}
.quick-links{left:161px}
.quick-links a{display:block;font-size:11.5px;line-height:19px;color:#ddd}
.contact{left:454px}
.contact-row{display:flex;gap:10px;font-size:11px;line-height:16px;margin-bottom:14px}
.footer-mark{position:absolute;left:780px;top:60px;display:flex;align-items:center;gap:14px;font-family:"Lato",sans-serif;font-weight:700;font-size:30px;color:#4a4a4a}
.footer-mark i{display:block;width:60px;height:60px;border-radius:50%;background:#3e3e3e}
.footer-bar{top:3674px;height:45px;background:var(--footer-bar);color:#bbb;font-size:11px}
.footer-bar .copy{position:absolute;left:161px;top:15px}
.social{position:absolute;right:160px;top:11px;display:flex;gap:8px}
.social i{display:block;width:22px;height:22px;background:#444;border-radius:2px}
</style>
</head>
<body>

<header class="section site-header">
  <div class="brand"><span class="brand-dot"></span>Carla Wendt</div>
  <nav class="main-nav">
    <span class="nav-home"><svg width="14" height="14" viewBox="0 0 14 14"><path d="M1 7 L7 1 L13 7 M3 6 V13 H11 V6" fill="none" stroke="#fff" stroke-width="2"/></svg></span>
    <a>About Us</a><a>Coaching programs</a><a>Speaking</a><a>Store</a><a>Blog</a><a>Contact Us</a>
    <span class="nav-search"><svg width="12" height="12" viewBox="0 0 12 12"><circle cx="5" cy="5" r="3.5" fill="none" stroke="#555" stroke-width="1.5"/><path d="M7.5 7.5 L11 11" stroke="#555" stroke-width="1.5"/></svg></span>
  </nav>
</header>

<section class="section hero">
  <div class="ph hero-bg" role="img" aria-label="Library aisle with bookshelves, softly blurred"></div>
  <svg class="arrow" style="left:100px" width="30" height="60" viewBox="0 0 30 60"><path d="M26 4 L6 30 L26 56" fill="none" stroke="#fff" stroke-width="3"/></svg>
  <svg class="arrow" style="left:1060px" width="30" height="60" viewBox="0 0 30 60"><path d="M4 4 L24 30 L4 56" fill="none" stroke="#fff" stroke-width="3"/></svg>
  <div class="hero-copy">
    <h1 class="hero-title">LEARNING ANY WHERE ANY TIME</h1>
    <p class="hero-sub">We Help Students Reach Theri Life Goals Faster<br>And More Efficiently.</p>
    <div class="hero-actions"><span class="btn btn-green">Buy today !</span><span class="btn btn-outline">Contact now!</span></div>
  </div>
  <div class="ph hero-book" role="img" aria-label="Book cover of Ladder to Campus with author portrait"><span>By Carla Wendt</span></div>
</section>

<section class="section welcome">
  <div class="ph welcome-media" role="img" aria-label="Introductory video still of the author"></div>
  <div class="welcome-text">
    <h2>WELCOME TO <b>CARLA WENDT</b></h2>
    <p>Carla Wendt is a certified teacher and holds advanced certification in academic coaching and tutoring. She also is a certified trainer in the Morris Pelley Growth Method. She has three successful adult children, and helped them overcome learning differences and thrive.</p>
    <p>Carla's approach is whole person oriented. Her programs help students learn life skills in addition to the study, time management skills, etc. offered by most academic coaching programs.</p>
    <span class="btn btn-purple">Read more</span>
  </div>
</section>

<section class="section learning">
  <div class="ph learning-photo" role="img" aria-label="Two smiling students carrying backpacks and books"></div>
  <div class="learning-copy">
    <h2>LEARNING WITHOUT LIMITS</h2>
    <p>It is a long established fact that a reader will be distracted by the readable content of a page when looking at its layout</p>
    <div class="learning-actions"><span class="btn btn-purple">Get start now</span><span class="btn btn-purple">Shop now</span></div>
  </div>
</section>

<section class="section programs">
  <h2 class="section-title">OUR PROGRAMS</h2>
  <p class="section-lead">Lorem Ipsum is simply dummy text of the printing and typesetting industry. Lorem Ipsum has been the industry's</p>
  <div class="program-card coaching">
    <svg width="44" height="40" viewBox="0 0 44 40"><circle cx="16" cy="10" r="7" fill="none" stroke="#fff" stroke-width="2.5"/><circle cx="30" cy="14" r="6" fill="none" stroke="#fff" stroke-width="2.5"/><path d="M3 36 C3 24 29 24 29 36 Z M24 36 C26 28 42 28 42 36" fill="none" stroke="#fff" stroke-width="2.5"/></svg>
    <h3>COACHING PROGRAMS</h3>
    <p>Lorem Ipsum is simply dummy text of the printing and typesetting industry. Lorem Ipsum has been the industry's</p>
    <span class="card-btn">Read More &#9656;</span>
  </div>
  <div class="program-card speaking">
    <svg width="44" height="40" viewBox="0 0 44 40"><rect x="20" y="2" width="22" height="14" rx="2" fill="none" stroke="#fff" stroke-width="2.5"/><circle cx="14" cy="18" r="6" fill="none" stroke="#fff" stroke-width="2.5"/><path d="M2 38 C2 26 26 26 26 38 Z" fill="none" stroke="#fff" stroke-width="2.5"/></svg>
    <h3>SPEAKING PROGRAMS</h3>
    <p>Lorem Ipsum is simply dummy text of the printing and typesetting industry. Lorem Ipsum has been the industry's</p>
    <span class="card-btn">Read More &#9656;</span>
  </div>
</section>

<section class="section shop">
  <div class="shop-panel"></div>
  <div class="shop-copy">
    <h2>SHOP</h2>
    <p>Ladder to Campus<br>Steps and strategies to prepare you to thrive in college and beyond<br>Available 12/01/2017</p>
    <div class="shop-actions"><span class="btn btn-green">View shop</span><span class="btn btn-green">Download preview chapter</span></div>
  </div>
  <div class="shop-tile" style="left:600px;top:0;background:linear-gradient(135deg,#a6543c,#d9b8a0 55%,#3b3b45)" role="img" aria-label="Student standing by a brick wall"><span class="label">1 Chapter Available</span></div>
  <div class="shop-tile" style="left:900px;top:0;background:linear-gradient(135deg,#6f8f5a,#d8c3ae 55%,#4a5a3a)" role="img" aria-label="Student smiling outdoors"><span class="label">2 Chapter Available</span></div>
  <div class="shop-tile" style="left:600px;top:250px;background:linear-gradient(135deg,#3d6fb0,#e1a06a 50%,#c23a3a)" role="img" aria-label="Group of cheerful students"><span class="label">3 Chapter Available</span></div>
  <div class="shop-tile" style="left:900px;top:250px;background:linear-gradient(135deg,#9a8a78,#e8e0d4 50%,#5d5248)" role="img" aria-label="Students studying at a table"><span class="label">4 Chapter Available</span></div>
</section>

<section class="section blog">
  <h2 class="section-title">LETEST BLOG</h2>
  <svg style="position:absolute;left:112px;top:236px" width="20" height="36" viewBox="0 0 20 36"><path d="M17 2 L3 18 L17 34" fill="none" stroke="#999" stroke-width="3"/></svg>
  <svg style="position:absolute;left:1060px;top:236px" width="20" height="36" viewBox="0 0 20 36"><path d="M3 2 L17 18 L3 34" fill="none" stroke="#999" stroke-width="3"/></svg>
  <article class="blog-main">
    <div class="copy">
      <h3>Lorem ipsum dolor sit amet, consectetuer</h3>
      <p class="posted"><b>Posted by :</b> Admin</p>
      <p>Since moving to digital photos years back, I have developed a happy finger when it comes to taking pictures, so going thru all the pictures that I Lorem ipsum dolor sit amet, consectetuer adipiscing elit, sed diam nonummy nibh.</p>
      <span class="read-more">Read More &#10230;</span>
    </div>
    <div class="ph thumb" role="img" aria-label="Hand writing in a notebook">
      <span class="date-tag">30 JUN<br>2017</span>
    </div>
  </article>
  <article class="blog-side" style="top:124px">
    <div class="ph thumb" role="img" aria-label="Students with laptops"><span class="date-tag">29 Jun<br>2017</span></div>
    <div class="copy"><h4>Lorem ipsum dolor sit amet, consectetuer</h4><p>Since moving to digital photos years back...</p><span class="read-more">Read More &#10230;</span></div>
  </article>
  <article class="blog-side" style="top:267px">
    <div class="ph thumb" role="img" aria-label="Classroom lecture scene"><span class="date-tag">28 Jun<br>2017</span></div>
    <div class="copy"><h4>Lorem ipsum dolor sit amet, consectetuer</h4><p>Since moving to digital photos years back...</p><span class="read-more">Read More &#10230;</span></div>
  </article>
</section>

<section class="section newsletter">
  <h2>Subscribe To Our Newsletter</h2>
  <p>Sign Up To Receive Email Updates About Courses</p>
  <div class="subscribe-form"><span class="subscribe-input">Enter your email</span><span class="subscribe-btn">Subscribe</span></div>
</section>

<section class="section students">
  <h2>OUR HAPPY STUDENTS</h2>
  <p class="quote">Lorem Ipsum is simply dummy text of the printing and typesetting industry. Lorem Ipsum has been the industry's standard dummy text ever since the 1500s, when an unknown printer took a galley of type and scrambled it to make a type specimen book. It has survived not only five centuries, but also the leap into electronic typesetting, remaining essentially unchanged. It was popularised in the 1960s with the release of sheets containing Lorem Ipsum passages, and more recently with desktop publishing software including versions of Lorem Ipsum.</p>
  <p class="name">Mr Lorem Lpsum</p>
  <p class="role">Creative Manager</p>
  <div class="dots"><i></i><i></i><i></i></div>
  <div class="ph students-photo" role="img" aria-label="Group of joyful students jumping together"></div>
</section>

<footer class="section site-footer">
  <div class="footer-col quick-links">
    <h4>Quick Links</h4><div class="rule"></div>
    <a>Home</a><a>About Us</a><a>Coaching programs</a><a>Speaking</a><a>Store</a><a>Blog</a><a>Contact Us</a>
  </div>
  <div class="footer-col contact">
    <h4>Contact Us</h4><div class="rule"></div>
    <div class="contact-row"><svg width="12" height="14" viewBox="0 0 12 14"><path d="M6 13 C2 8 1 6 1 5 A5 5 0 0 1 11 5 C11 6 10 8 6 13 Z" fill="#aaa"/><circle cx="6" cy="5" r="1.8" fill="#2a2a2a"/></svg><span>CARLAWENDT<br>lorem Ipsum dolor Ipsum volt<br>amet dolor - 123456</span></div>
    <div class="contact-row"><svg width="12" height="12" viewBox="0 0 12 12"><path d="M2 1 L4.5 1 L5.5 4 L4 5 C5 7 6 8 7 8.5 L8 7 L11 8 L11 10.5 C6 11 1 6 2 1 Z" fill="#aaa"/></svg><span>(65) 6000 1482</span></div>
    <div class="contact-row"><svg width="13" height="10" viewBox="0 0 13 10"><rect x=".5" y=".5" width="12" height="9" fill="none" stroke="#aaa"/><path d="M.5 .5 L6.5 5.5 L12.5 .5" fill="none" stroke="#aaa"/></svg><span>info@carlawendt.example</span></div>
  </div>
  <div class="footer-mark"><i></i>Carla Wendt</div>
</footer>
<div class="section footer-bar">
  <span class="copy">Copyright © CARLAWENDT All Rights Reserved</span>
  <div class="social"><i></i><i></i><i></i><i></i></div>
</div>

</body>
</html>
```